Pre-Paid Card for Teens needs a design

We are a Fintech company called Tallowen. We will sell prepaid cards for families and teens. Now we need a prepaid card design. Prepaid card should have a paywheel logo, company logo, 16 card number, expire date. Our webpage is http://www.velorant-example.com
Target Market(s)
Teenages between 8 - 18 years old
Industry/Entity Type
It Company
Requirements
Must have
- The prepaid card must include tallowen logo, paywheel debit card logo (I already attached a sample card), 16 digit card number and expire date.
Nice to have
- It should be fun and prestigious for young people.
Should not have
- We don't want that the card has a lots of color

```html
<!DOCTYPE html>
<html lang="en">
<head>
<meta charset="utf-8">
<title>Tallowen Prepaid Card</title>
<link rel="stylesheet" href="https://fonts.googleapis.com/css2?family=Share+Tech+Mono&family=Roboto+Condensed:wght@500&display=swap">
<style>
  :root {
    --page-bg: #ffffff;
    --card-dark: #3a3a3a;
    --card-mid: #505050;
    --card-light: #8a8a8a;
    --frame-line: #1e1e1e;
    --brand-mark: #6a6a6a;
    --brand-text: #e6e6e6;
    --emboss-face: #ececec;
    --emboss-dark: #1a1a1a;
    --emboss-light: #ffffff;
    --label-text: #f2f2f2;
    --network-mark: #777777;
    --network-text: #ffffff;
  }
  * { margin: 0; padding: 0; box-sizing: border-box; }
  html, body {
    width: 1200px;
    height: 835px;
    overflow: hidden;
    background: var(--page-bg);
  }
  .canvas {
    position: relative;
    width: 1200px;
    height: 835px;
  }
  .card {
    position: absolute;
    left: 82px;
    top: 93px;
    width: 1010px;
    height: 635px;
    border-radius: 14px;
    overflow: hidden;
    box-shadow: 6px 8px 10px rgba(0, 0, 0, 0.45);
  }
  .card-surface {
    position: absolute;
    inset: 0;
    background:
      linear-gradient(115deg, var(--card-dark) 0%, var(--card-mid) 45%, var(--card-light) 80%, var(--card-mid) 100%);
  }
  .card-frame {
    position: absolute;
    inset: 0;
  }
  .brand {
    position: absolute;
    left: 58px;
    top: 58px;
    display: flex;
    align-items: center;
    gap: 58px;
  }
  .brand-square {
    width: 84px;
    height: 84px;
    border-radius: 6px;
    background: var(--brand-mark);
  }
  .brand-name {
    font-family: "Roboto Condensed", sans-serif;
    font-weight: 500;
    font-size: 52px;
    color: var(--brand-text);
    letter-spacing: 2px;
  }
  .embossed {
    font-family: "Share Tech Mono", monospace;
    color: var(--emboss-face);
    text-shadow:
      -1px -1px 0 var(--emboss-light),
      2px 2px 1px var(--emboss-dark),
      3px 3px 3px rgba(0, 0, 0, 0.5);
  }
  .card-number {
    position: absolute;
    left: 38px;
    top: 382px;
    display: flex;
    gap: 56px;
    font-size: 54px;
    letter-spacing: 10px;
  }
  .expiry {
    position: absolute;
    left: 483px;
    top: 470px;
    display: flex;
    align-items: center;
    gap: 24px;
  }
  .expiry-label {
    font-family: "Roboto Condensed", sans-serif;
    font-weight: 500;
    font-size: 15px;
    line-height: 16px;
    letter-spacing: 1.5px;
    color: var(--label-text);
    text-align: center;
  }
  .expiry-date {
    font-size: 38px;
    letter-spacing: 4px;
  }
  .holder-name {
    position: absolute;
    left: 46px;
    top: 542px;
    font-size: 48px;
    letter-spacing: 14px;
  }
  .network {
    position: absolute;
    left: 775px;
    top: 510px;
    display: flex;
    align-items: center;
    gap: 10px;
  }
  .network-dot {
    width: 72px;
    height: 72px;
    border-radius: 50%;
    background: var(--network-mark);
  }
  .network-name {
    font-family: "Roboto Condensed", sans-serif;
    font-weight: 500;
    font-size: 30px;
    color: var(--network-text);
  }
</style>
</head>
<body>
  <main class="canvas">
    <section class="card" aria-label="Tallowen prepaid card">
      <div class="card-surface" role="img" aria-label="Brushed dark grey metallic surface with faceted angular shapes"></div>

      <svg class="card-frame" width="1010" height="635" viewBox="0 0 1010 635" aria-hidden="true">
        <polyline points="0,105 30,105 30,51 490,51 490,105 1010,105"
                  fill="none" stroke="var(--frame-line)" stroke-width="2"/>
      </svg>

      <div class="brand">
        <div class="brand-square"></div>
        <span class="brand-name">tallowen</span>
      </div>

      <div class="card-number embossed">
        <span>1234</span><span>1234</span><span>1234</span><span>1234</span>
      </div>

      <div class="expiry">
        <div class="expiry-label">VALID<br>THRU</div>
        <div class="expiry-date embossed">12/08</div>
      </div>

      <div class="holder-name embossed">OWEN HALDER</div>

      <div class="network">
        <div class="network-dot"></div>
        <span class="network-name">Paywheel</span>
      </div>
    </section>
  </main>
</body>
</html>
```